Halvorsen Business Card/Stationary
Halvorsen
Project: Halvorsen Business Card/Stationary
Halvorsen Business Card/Stationary -
Creative Brief
Professional
R. Gordon Halvorsen
President
3847 Marlow Bend P.O. Box 6194 Sandusky, Ohio 44915
ghalvorsen@halvorsenllc.example
www.halvorsenllc.example

```html
<!DOCTYPE html>
<html lang="en">
<head>
<meta charset="utf-8">
<title>Halvorsen Business Card</title>
<link href="https://fonts.googleapis.com/css2?family=Open+Sans:wght@400;600;700;800&display=swap" rel="stylesheet">
<style>
  :root {
    --page: #ffffff;
    --card: #000000;
    --text: #ffffff;
    --muted: #d9d9d9;
    --mark: #c9c9c9;
    --mark-shape: #7d7d7d;
  }
  * { margin: 0; padding: 0; box-sizing: border-box; }
  html, body {
    width: 1200px; height: 852px; overflow: hidden;
    background: var(--page);
    font-family: "Open Sans", Arial, sans-serif;
  }
  .canvas { position: relative; width: 1200px; height: 852px; }
  .business-card {
    position: absolute; left: 220px; top: 208px;
    width: 768px; height: 467px;
    background: var(--card); color: var(--text);
  }
  .brand-shape {
    position: absolute; left: 155px; top: 100px;
    width: 170px; height: 170px; border-radius: 50%;
    background: var(--mark-shape);
  }
  .brand-name {
    position: absolute; left: 40px; top: 292px; width: 400px;
    text-align: center;
    font-weight: 800; font-size: 50px; line-height: 1; letter-spacing: 3px;
    color: var(--mark);
  }
  .holder { position: absolute; left: 500px; top: 84px; }
  .holder-name { font-weight: 700; font-size: 21px; line-height: 1.2; }
  .holder-title { font-size: 19px; line-height: 1.3; color: var(--muted); }
  .address {
    position: absolute; left: 500px; top: 203px;
    font-style: normal;
    font-size: 14px; line-height: 20px; color: var(--muted);
  }
  .contact-list {
    position: absolute; left: 500px; top: 302px;
    list-style: none; font-size: 14px; line-height: 22.5px; color: var(--muted);
  }
  .contact-list li { display: flex; align-items: center; gap: 7px; }
  .contact-icon { width: 11px; height: 11px; fill: var(--muted); flex: none; }
</style>
</head>
<body>
<div class="canvas">
  <section class="business-card">
    <div class="brand-shape" aria-hidden="true"></div>
    <div class="brand-name">HALVORSEN</div>

    <div class="holder">
      <p class="holder-name">R. Gordon Halvorsen</p>
      <p class="holder-title">President</p>
    </div>

    <address class="address">
      3847 Marlow Bend<br>
      P.O. Box 6194<br>
      Sandusky, Ohio 44915
    </address>

    <ul class="contact-list">
      <li>
        <svg class="contact-icon" viewBox="0 0 12 12"><path d="M2.5 0.8l2 2.2-1 1.3c.7 1.5 1.8 2.6 3.3 3.3l1.3-1 2.2 2-1.2 2.4C5 10.8 1.2 7 0.1 2z"/></svg>
        <span>1 419 555 0148</span>
      </li>
      <li>
        <svg class="contact-icon" viewBox="0 0 12 12"><rect x="3" y="0" width="6" height="12" rx="1"/><rect x="4" y="1.5" width="4" height="7" fill="#000"/></svg>
        <span>1 419 555 0193</span>
      </li>
      <li>
        <svg class="contact-icon" viewBox="0 0 12 12"><rect x="3" y="0.5" width="6" height="4"/><rect x="0.5" y="4.5" width="11" height="5" rx="1"/><rect x="3" y="8" width="6" height="3.5"/></svg>
        <span>1419 555 0148</span>
      </li>
      <li>
        <svg class="contact-icon" viewBox="0 0 12 12"><rect x="0.5" y="2" width="11" height="8"/><path d="M0.5 2l5.5 4.5L11.5 2" stroke="#000" stroke-width="1" fill="none"/></svg>
        <span>ghalvorsen@halvorsenllc.example</span>
      </li>
      <li>
        <svg class="contact-icon" viewBox="0 0 12 12"><circle cx="6" cy="6" r="5.5"/></svg>
        <span>www.halvorsenllc.example</span>
      </li>
    </ul>
  </section>
</div>
</body>
</html>
```